Business card design needed

New company based in Brisbane, Australia. Brindle Technologies. The business is focused on the delivery of network architecture design and deployment. We will provide both services and the sale of the necessary equipment to deliver the service. Cloud computing is an important element of our focus as this is an emerging market for enterprises in Queensland. Our target marketplace is medium to large corporations with complex infrastructure requirements. IT Management and above will be the typical entry point for us into these accounts. We would like to see the use of various shade of green, design should be clutter free and impress stability, trust and growth.
Updates
Hey Everyone
Just we let you all know we have changed this project to 'committed' payment status.
Looking forward to seeing the designs! Thanks for your efforts.
Best Regards
Martin
Industry/Entity Type
Architecture
Contact Information for Business Card
Brindle Technologies, Martin Coulter, Sales Director, Level 19 Harwell Court, 58 Kelvane Street, Brisbane QLD 4000, Ph +61 7 3946 2271, M +61 4 4208 6157, E martin.coulter@brindletechnologies-example.com.au
Look and feel
Each slider illustrates characteristics of the customer's brand and the style your logo design should communicate.

```html
<!DOCTYPE html>
<html lang="en">
<head>
<meta charset="utf-8">
<title>Brindle Technologies – Business Card</title>
<link rel="stylesheet" href="https://fonts.googleapis.com/css2?family=Saira+Condensed:wght@300;600&family=Kelly+Slab&family=Exo+2:ital,wght@1,300&display=swap">
<style>
  :root {
    --brand-green: #2a8a4a;
    --text-grey: #5b5b5d;
    --icon-grey: #5f5f61;
    --card-white: #ffffff;
    --surround: #f3f3f3;
    --edge: #d6d6d6;
  }
  * { margin: 0; padding: 0; box-sizing: border-box; }
  html, body {
    width: 1200px;
    height: 716px;
    overflow: hidden;
    background: var(--surround);
  }
  .card {
    position: absolute;
    left: 23px;
    top: 27px;
    width: 1149px;
    height: 664px;
    background: var(--card-white);
    border: 1px solid var(--edge);
    overflow: hidden;
  }
  .company-name {
    position: absolute;
    right: 57px;
    top: 56px;
    font-family: "Saira Condensed", sans-serif;
    font-weight: 600;
    font-size: 80px;
    line-height: 1;
    letter-spacing: 2px;
    color: var(--brand-green);
    text-transform: uppercase;
    white-space: nowrap;
  }
  .rule {
    position: absolute;
    left: 64px;
    top: 164px;
    width: 1048px;
    height: 4px;
  }
  .person-name {
    position: absolute;
    left: 64px;
    top: 262px;
    font-family: "Kelly Slab", sans-serif;
    font-weight: 400;
    font-size: 48px;
    line-height: 1;
    letter-spacing: 1px;
    color: var(--brand-green);
    white-space: nowrap;
  }
  .job-title {
    position: absolute;
    left: 64px;
    top: 326px;
    font-family: "Saira Condensed", sans-serif;
    font-weight: 300;
    font-size: 38px;
    line-height: 1;
    letter-spacing: 0.5px;
    color: var(--brand-green);
    white-space: nowrap;
  }
  .contact-list {
    position: absolute;
    left: 48px;
    top: 446px;
    list-style: none;
  }
  .contact-item {
    display: flex;
    align-items: center;
    height: 56px;
  }
  .contact-icon {
    width: 38px;
    height: 38px;
    flex: none;
    margin-right: 18px;
  }
  .contact-text {
    font-family: "Exo 2", sans-serif;
    font-style: italic;
    font-weight: 300;
    font-size: 34px;
    line-height: 1;
    color: var(--text-grey);
    white-space: nowrap;
  }
</style>
</head>
<body>
  <main class="card">
    <h1 class="company-name">Brindle Technologies</h1>

    <svg class="rule" viewBox="0 0 1048 4" aria-hidden="true">
      <line x1="0" y1="2" x2="1048" y2="2" stroke="var(--brand-green)" stroke-width="4" stroke-dasharray="8 6"/>
    </svg>

    <h2 class="person-name">Martin Coulter</h2>
    <p class="job-title">Sales Director</p>

    <ul class="contact-list">
      <li class="contact-item">
        <svg class="contact-icon" viewBox="0 0 40 40" aria-label="Address">
          <circle cx="20" cy="20" r="20" fill="var(--icon-grey)"/>
          <path d="M20 9a8 8 0 0 0-8 8c0 6 8 15 8 15s8-9 8-15a8 8 0 0 0-8-8zm0 11a3 3 0 1 1 0-6 3 3 0 0 1 0 6z" fill="#fff"/>
        </svg>
        <span class="contact-text">Level 19 Harwell Court - 58 Kelvane Street - Brisbane QLD 4000</span>
      </li>
      <li class="contact-item">
        <svg class="contact-icon" viewBox="0 0 40 40" aria-label="Phone">
          <circle cx="20" cy="20" r="20" fill="var(--icon-grey)"/>
          <path d="M13 10l4 -1 3 6-2.5 2c1 2.5 3 4.5 5.5 5.5l2-2.5 6 3-1 4c-9 1-18-8-17-17z" fill="#fff"/>
        </svg>
        <span class="contact-text">Ph +61 7 3946 2271 - M +61 4 4208 6157</span>
      </li>
      <li class="contact-item">
        <svg class="contact-icon" viewBox="0 0 40 40" aria-label="Email">
          <circle cx="20" cy="20" r="20" fill="var(--icon-grey)"/>
          <path d="M14.5 21.5h11.5c.6-4.5-1.8-8-6-8-4.6 0-7.8 4.2-7.8 8.8 0 3.6 2.4 5.9 5.8 5.9 2 0 3.7-.6 5-1.6l-1-2.3c-1 .7-2.2 1.1-3.5 1.1-2.1 0-3.7-1.3-4-3.9zm.5-2.8c.7-2 2.3-3.3 4.4-3.3 1.9 0 3 1.3 3 3.3z" fill="#fff"/>
        </svg>
        <span class="contact-text">martin.coulter@brindletechnologies-example.com.au</span>
      </li>
    </ul>
  </main>
</body>
</html>
```